BrambleWorks business card

Looking for business card design that supports our company/software values. We have 2 logo designs at the moment but open to change if you think you can enhance the brand. Check out website www.brambleworks.com.au.

Target Market(s)

Education

Contact Information for Business Card

Name, title, mobile, email and website

Font styles to use
Sans Serif

Colors

Designer to choose colors to be used in the design.

Requirements
Must have
• BrambleWorks logo with tree and tagline on rear side with dark grey background colour

```html
<!DOCTYPE html>
<html lang="en">
<head>
<meta charset="utf-8">
<title>BrambleWorks business card</title>
<link rel="stylesheet" href="https://fonts.googleapis.com/css2?family=Open+Sans:wght@400;700&family=Ubuntu:wght@400&display=swap">
<style>
  :root {
    --page-bg: #f4f4f4;
    --card-white: #ffffff;
    --card-grey: #636462;
    --ink-grey: #5e5f5d;
    --brand-green: #4e9230;
    --rule-grey: #8a8a8a;
    --on-dark: #f4f4f4;
  }
  * { margin: 0; padding: 0; box-sizing: border-box; }
  html, body {
    width: 1200px; height: 1200px; overflow: hidden;
    background: var(--page-bg);
  }
  .stage { position: relative; width: 1200px; height: 1200px; }
  .card {
    position: absolute; left: 272px; width: 652px; height: 390px;
    box-shadow: 22px 22px 18px rgba(0,0,0,0.32);
  }
  .card--front { top: 182px; background: var(--card-white); }
  .card--back { top: 635px; background: var(--card-grey); }

  .holder { position: absolute; left: 28px; top: 36px; font-family: "Open Sans", sans-serif; }
  .holder__name { font-weight: 700; font-size: 26px; color: var(--ink-grey); line-height: 1.2; }
  .holder__title { font-size: 19px; color: var(--brand-green); line-height: 1.2; margin-top: 1px; }
  .holder__bar { width: 38px; height: 4px; background: var(--ink-grey); margin-top: 11px; }

  .brand-front {
    position: absolute; right: 30px; top: 22px; width: 240px;
    font-family: "Ubuntu", sans-serif; color: var(--ink-grey); text-align: right;
  }
  .brand-front__name { font-size: 40px; line-height: 1; white-space: nowrap; }
  .brand-front__rule { height: 2px; background: var(--rule-grey); margin-top: 8px; }
  .brand-front__tagline { font-size: 17px; margin-top: 5px; white-space: nowrap; }

  .contacts {
    position: absolute; left: 28px; top: 232px; list-style: none;
    font-family: "Open Sans", sans-serif; font-size: 18px; color: var(--ink-grey);
  }
  .contacts__item { display: flex; align-items: center; height: 24.6px; }
  .contacts__icon { width: 18px; height: 18px; margin-right: 10px; fill: var(--brand-green); }

  .brand-back {
    position: absolute; left: 0; right: 0; top: 118px;
    display: flex; justify-content: center; align-items: center; gap: 28px;
    font-family: "Ubuntu", sans-serif; color: var(--on-dark);
  }
  .brand-back__mark { width: 70px; height: 70px; border-radius: 50%; background: var(--brand-green); flex: none; }
  .brand-back__name { font-size: 48px; line-height: 1; white-space: nowrap; }
  .brand-back__rule { height: 2px; background: var(--on-dark); margin-top: 10px; }
  .brand-back__tagline { font-size: 21px; margin-top: 6px; text-align: center; white-space: nowrap; }
  .back-web {
    position: absolute; left: 0; right: 0; top: 342px; text-align: center;
    font-family: "Ubuntu", sans-serif; font-size: 19px; color: var(--on-dark);
  }
</style>
</head>
<body>
<main class="stage">
  <section class="card card--front" aria-label="Business card front">
    <div class="holder">
      <p class="holder__name">Daniel Harper</p>
      <p class="holder__title">Director</p>
      <div class="holder__bar"></div>
    </div>

    <div class="brand-front">
      <p class="brand-front__name">BrambleWorks</p>
      <div class="brand-front__rule"></div>
      <p class="brand-front__tagline">Student Success Platform</p>
    </div>

    <ul class="contacts">
      <li class="contacts__item">
        <svg class="contacts__icon" viewBox="0 0 24 24" aria-hidden="true"><path d="M6.6 10.8a15.1 15.1 0 0 0 6.6 6.6l2.2-2.2c.3-.3.7-.4 1-.2 1.1.4 2.3.6 3.6.6.6 0 1 .4 1 1V20c0 .6-.4 1-1 1C10.6 21 3 13.4 3 4c0-.6.4-1 1-1h3.5c.6 0 1 .4 1 1 0 1.3.2 2.5.6 3.6.1.3 0 .7-.2 1z"/></svg>
        <span>123.456.789.</span>
      </li>
      <li class="contacts__item">
        <svg class="contacts__icon" viewBox="0 0 24 24" aria-hidden="true"><path d="M7 1h10a2 2 0 0 1 2 2v18a2 2 0 0 1-2 2H7a2 2 0 0 1-2-2V3a2 2 0 0 1 2-2zm0 3v14h10V4zm5 15.5a1 1 0 1 0 0 2 1 1 0 0 0 0-2z"/></svg>
        <span>123.456.789.</span>
      </li>
      <li class="contacts__item">
        <svg class="contacts__icon" viewBox="0 0 24 24" aria-hidden="true"><path d="M2 5h20v14H2zm2 2v.4l8 5.2 8-5.2V7zm0 2.8V17h16V9.8l-8 5.2z"/></svg>
        <span>info@brambleworks.com.au</span>
      </li>
      <li class="contacts__item">
        <svg class="contacts__icon" viewBox="0 0 24 24" aria-hidden="true"><path d="M12 2a10 10 0 1 0 0 20 10 10 0 0 0 0-20zm6.9 6h-2.9a15.6 15.6 0 0 0-1.4-3.6A8 8 0 0 1 18.9 8zM12 4c.8 1.2 1.5 2.5 1.9 4h-3.8c.4-1.5 1.1-2.8 1.9-4zM4.3 14a8.2 8.2 0 0 1 0-4h3.4a16.5 16.5 0 0 0 0 4zm.8 2h2.9c.3 1.3.8 2.5 1.4 3.6A8 8 0 0 1 5.1 16zM8 8H5.1a8 8 0 0 1 4.3-3.6C8.8 5.5 8.3 6.7 8 8zm4 12c-.8-1.2-1.5-2.5-1.9-4h3.8c-.4 1.5-1.1 2.8-1.9 4zm2.3-6H9.7a14.7 14.7 0 0 1 0-4h4.6a14.7 14.7 0 0 1 0 4zm.3 5.6c.6-1.1 1.1-2.3 1.4-3.6h2.9a8 8 0 0 1-4.3 3.6zm1.7-5.6a16.5 16.5 0 0 0 0-4h3.4a8.2 8.2 0 0 1 0 4z"/></svg>
        <span>www.brambleworks.com.au</span>
      </li>
    </ul>
  </section>

  <section class="card card--back" aria-label="Business card back">
    <div class="brand-back">
      <div class="brand-back__mark"></div>
      <div class="brand-back__text">
        <p class="brand-back__name">BrambleWorks</p>
        <div class="brand-back__rule"></div>
        <p class="brand-back__tagline">Student Success Platform</p>
      </div>
    </div>
    <p class="back-web">www.brambleworks.com.au</p>
  </section>
</main>
</body>
</html>
```